Course Graduation Certificate

This project is not for a flyer but instead for the creation of a course graduation certificate. The final certificate needs to include the Marlowe Summit Aviation Academy logo and the text stating as follows:
Certifies that ___________________________ has satisfactorily completed the course of _______________________________ on ________________________________
I would also like to include some type of gold seal of completion as well as a place to sign my name and credentials at the bottom of the certificate
I have included the Marlowe Summit Aviation Academy logo as well as three other certificate examples for you to work from.
Target Market(s)
Students completing a certification course and receiving a certificate
Look and feel

```html
<!DOCTYPE html>
<html lang="en">
<head>
<meta charset="utf-8">
<title>Course Completion Certificate – Marlowe Summit Aviation Academy</title>
<link rel="stylesheet" href="https://fonts.googleapis.com/css2?family=UnifrakturCook:wght@700&family=Tinos:ital@1&family=Outfit:wght@400;600&display=swap">
<style>
  :root {
    --paper: #ffffff;
    --ink: #111111;
    --cobalt: #0a5fae;
    --cobalt-deep: #064b86;
    --gold: #b38b4d;
    --gold-light: #f3d27a;
    --gold-dark: #9a6a1c;
    --rule: #555555;
  }
  html, body {
    margin: 0;
    padding: 0;
    width: 1200px;
    height: 927px;
    overflow: hidden;
    background: var(--paper);
  }
  .certificate {
    position: relative;
    width: 1200px;
    height: 927px;
    background: var(--paper);
    overflow: hidden;
  }
  .certificate-art {
    position: absolute;
    inset: 0;
  }
  .title {
    position: absolute;
    left: 410px;
    top: 140px;
    width: 690px;
    margin: 0;
    text-align: center;
    font-family: "UnifrakturCook", serif;
    font-weight: 700;
    font-size: 62px;
    line-height: 1;
    color: var(--ink);
  }
  .statement {
    position: absolute;
    margin: 0;
    font-family: "Tinos", "Times New Roman", serif;
    font-style: italic;
    font-size: 33px;
    line-height: 1;
    color: var(--ink);
    white-space: nowrap;
  }
  .statement--certifies { left: 420px; top: 316px; }
  .statement--has { left: 1037px; top: 316px; }
  .statement--course { left: 398px; top: 426px; }
  .statement--on { left: 546px; top: 536px; }
  .fill-line {
    position: absolute;
    height: 0;
    border-top: 1px solid var(--rule);
  }
  .fill-line--name { left: 640px; top: 343px; width: 349px; }
  .fill-line--course { left: 757px; top: 459px; width: 349px; }
  .fill-line--date { left: 608px; top: 567px; width: 350px; }
  .fill-line--signature { left: 825px; top: 782px; width: 294px; }
  .academy-name {
    position: absolute;
    left: 394px;
    top: 726px;
    width: 230px;
    margin: 0;
    font-family: "Outfit", sans-serif;
    font-weight: 600;
    font-size: 21px;
    line-height: 1.15;
    color: var(--cobalt);
  }
  .signature-label {
    position: absolute;
    left: 859px;
    top: 713px;
    margin: 0;
    font-family: "Outfit", sans-serif;
    font-weight: 400;
    font-size: 23px;
    line-height: 1;
    color: var(--ink);
    letter-spacing: 0.2px;
  }
</style>
</head>
<body>
<main class="certificate">
  <svg class="certificate-art" width="1200" height="927" viewBox="0 0 1200 927" xmlns="http://www.w3.org/2000/svg">
    <defs>
      <linearGradient id="cobalt-panel" x1="0" y1="0" x2="0.4" y2="1">
        <stop offset="0" stop-color="#0a63b4"/>
        <stop offset="0.6" stop-color="#0a5aa6"/>
        <stop offset="1" stop-color="#064a84"/>
      </linearGradient>
      <radialGradient id="gold-seal" cx="0.45" cy="0.35" r="0.7">
        <stop offset="0" stop-color="#fbe6a6"/>
        <stop offset="0.5" stop-color="#d9a84a"/>
        <stop offset="1" stop-color="#9a6a1c"/>
      </radialGradient>
      <radialGradient id="gold-dust" cx="1" cy="0" r="1">
        <stop offset="0" stop-color="#e8d6a8" stop-opacity="0.55"/>
        <stop offset="1" stop-color="#e8d6a8" stop-opacity="0"/>
      </radialGradient>
      <linearGradient id="aircraft-tone" x1="0" y1="0" x2="1" y2="0">
        <stop offset="0" stop-color="#eeeeee" stop-opacity="0"/>
        <stop offset="0.5" stop-color="#e9e6e6" stop-opacity="0.7"/>
        <stop offset="1" stop-color="#eeeeee" stop-opacity="0"/>
      </linearGradient>
    </defs>

    <rect class="gold-dust" x="840" y="0" width="360" height="170" fill="url(#gold-dust)" role="img" aria-label="Faint scattered gold dot texture"/>

    <rect class="aircraft-backdrop" x="363" y="368" width="626" height="187" rx="80" fill="url(#aircraft-tone)" role="img" aria-label="Faint photograph of a passenger jet in flight"/>

    <g class="gold-frame" fill="none" stroke="var(--gold)">
      <path d="M380 44 H1128 Q1130 78 1165 80 V848 Q1130 850 1128 886 H380" stroke-width="3.4"/>
      <path d="M380 61.5 H1113 Q1115 90 1147 92 V836 Q1115 838 1113 869 H380" stroke-width="1.8"/>
    </g>

    <polygon class="cobalt-panel" points="0,0 431,0 219,464 423,927 0,927" fill="url(#cobalt-panel)"/>
    <polygon class="cobalt-shade" points="0,927 150,620 423,927" fill="#064b86" opacity="0.55"/>

    <circle class="seal-mount" cx="220" cy="464" r="161" fill="var(--paper)"/>
    <circle class="completion-seal" cx="224" cy="463" r="131" fill="url(#gold-seal)" role="img" aria-label="Gold completion seal with stars"/>

    <circle class="ribbon-seal" cx="720" cy="734" r="22" fill="url(#gold-seal)" role="img" aria-label="Gold award rosette with ribbons"/>
    <polygon class="ribbon-seal-tails" points="706,750 695,788 706,782 712,790 720,755 728,790 734,782 745,788 734,750" fill="#c9922f"/>
  </svg>

  <h1 class="title">Certificate Of Completion</h1>

  <p class="statement statement--certifies">Certifies that</p>
  <span class="fill-line fill-line--name"></span>
  <p class="statement statement--has">has</p>

  <p class="statement statement--course">completed the course of</p>
  <span class="fill-line fill-line--course"></span>

  <p class="statement statement--on">on</p>
  <span class="fill-line fill-line--date"></span>

  <p class="academy-name">Marlowe Summit Aviation Academy</p>

  <p class="signature-label">Authorized Signature</p>
  <span class="fill-line fill-line--signature"></span>
</main>
</body>
</html>
```